Non-profit organization requires InDesign based template for a educational booklet

***Overview***
Our business "The Southern Meridian Collective for Skills and Growth" is a not for profit organisation working in vocational education both in the Australian and international markets. While we work within many professional contexts, we also work with projects in developing countries assisting to build institutional capacity in the education industry, upskilling in disadvantaged communities to ultimately facilitate positive development outcomes.

Our project is looking to deliver agricultural-based education units that will be delivered in booklet form. Vocational students will use these unit booklets for self-paced or classroom group study. The front of each unit will have a nice graphical cover page, contents and details about learning in the unit. This will be followed by about 15 pages of educational content with plenty of pictures and other material such as tables and graphs to illustrate learning points. This will then be followed by a short question sheet with space for students to write answers, followed by Activity sheets where students put into practice skills from the unit.

***The designed template should have***
* Cover page;
* Content page;
* Two (2) different introduction pages (two for variation);
* Three (3) different pages for lesson text – these pages will be the main study pages for the students, 3 for variation;
* Activity page - like an activity worksheet;
* Question page - page with questions or reflections that the students need to answer - a space under each question for students to write;

***Design preferences***

*Font – an inDesign default font please like Calibri – text built on a base Normal font 11pt, then headings H1, H2 etc... from that basis e.g. 24pt for H1 etc... the size up to the designer.

Happy to see creativity of graphic artists with the above themes.

Target Market(s)

In the requested project, I require an Adobe InDesign template (file in .indd) to be designed that will have particular characteristics suited to students who are:

* Age 15-17;
* Have the educational equivalent to Australian and US education standard of Yr 8;
* Attending vocational school - vocational schools are between secondary high school and University and are usually used to produce graduates within the skill trade area;
* Agricultural theme in the template;
* Sustainability theme (agricultural sustainability) as well;

Students are from very poor rural farming families in growing rice, coconut, rambutan, mangoes, cocoa, palm oil... - very SE Asian agricultural landscape.

Students are used to black and white government textbooks which are very dry, largely dull in design and colour – we do not want this!

Industry/Entity Type

Agriculture

Font styles to use
Sans Serif

Colors

Designer to choose colors to be used in the design.

Requirements
Must have
• * Final file must be in an editable Adobe Indesign file (.indd), with editable layers;
• * SE Asian agricultural theme in the template;
• * design must not look like dull and boring textbooks or corporate training booklets; * design should be vibrant and interesting but also not distracting from the lesson (i.e. it is not too garish);
• * suitable colours (it will be printed full colour) easy on the eye for students of the age group - colours related to agriculture;
• *Modern look and feel;
Should not have
• * design must not look like dull and boring textbooks or corporate training booklets;

```html
<!DOCTYPE html>
<html lang="en">
<head>
<meta charset="utf-8">
<title>The Southern Meridian Collective for Skills and Growth – Booklet Cover</title>
<link rel="stylesheet" href="https://fonts.googleapis.com/css2?family=Roboto+Condensed:wght@700&display=swap">
<style>
  :root {
    --page: #ffffff;
    --forest: #006b5c;
    --forest-deep: #005a4d;
    --leaf-edge: #ffffff;
    --title: #ffffff;
    --gold: #f4c410;
    --amber: #f2a51c;
    --olive: #9db22c;
    --cream: #fbe9c2;
  }
  html, body {
    margin: 0;
    padding: 0;
    width: 1200px;
    height: 1200px;
    overflow: hidden;
    background: var(--page);
  }
  .canvas {
    position: relative;
    width: 1200px;
    height: 1200px;
    background: var(--page);
  }
  .cover {
    position: absolute;
    left: 219px;
    top: 61px;
    width: 762px;
    height: 1078px;
    overflow: hidden;
    background: var(--forest);
  }
  .cover-art {
    position: absolute;
    inset: 0;
    width: 762px;
    height: 1078px;
    display: block;
  }
  .cover-title {
    position: absolute;
    left: 126px;
    top: 100px;
    margin: 0;
    font-family: "Roboto Condensed", "Arial Narrow", sans-serif;
    font-weight: 700;
    font-size: 45px;
    line-height: 49.5px;
    letter-spacing: -0.5px;
    color: var(--title);
  }
  .cover-title span { display: block; }
</style>
</head>
<body>
<div class="canvas">
  <section class="cover">
    <svg class="cover-art" viewBox="0 0 826 1168" preserveAspectRatio="none" xmlns="http://www.w3.org/2000/svg">
      <defs>
        <linearGradient id="sweep-gold" x1="0" y1="0" x2="1" y2="0.4">
          <stop offset="0" stop-color="#2c7d55"/>
          <stop offset="0.45" stop-color="#9fb433"/>
          <stop offset="0.8" stop-color="var(--gold)"/>
          <stop offset="1" stop-color="#f2b414"/>
        </linearGradient>
        <linearGradient id="sweep-cream" x1="0" y1="0" x2="1" y2="0">
          <stop offset="0" stop-color="#ffffff"/>
          <stop offset="0.6" stop-color="#fdf4dc"/>
          <stop offset="1" stop-color="#f9e3a8"/>
        </linearGradient>
        <linearGradient id="sweep-olive" x1="0" y1="0" x2="1" y2="0">
          <stop offset="0" stop-color="#93ad2a"/>
          <stop offset="1" stop-color="#cfd462"/>
        </linearGradient>
        <linearGradient id="sweep-amber" x1="0" y1="0" x2="1" y2="1">
          <stop offset="0" stop-color="#f9d27a"/>
          <stop offset="0.6" stop-color="#f5b84a"/>
          <stop offset="1" stop-color="var(--amber)"/>
        </linearGradient>
        <linearGradient id="tone-stone" x1="0" y1="0" x2="1" y2="1">
          <stop offset="0" stop-color="#d9d4c8"/><stop offset="1" stop-color="#7a6450"/>
        </linearGradient>
        <linearGradient id="tone-terrace" x1="0" y1="0" x2="0" y2="1">
          <stop offset="0" stop-color="#9fb59a"/><stop offset="0.4" stop-color="#4f8a2a"/><stop offset="1" stop-color="#8cc43c"/>
        </linearGradient>
        <linearGradient id="tone-field" x1="0" y1="0" x2="1" y2="1">
          <stop offset="0" stop-color="#4c7d22"/><stop offset="1" stop-color="#96c040"/>
        </linearGradient>
        <linearGradient id="tone-coast" x1="0" y1="0" x2="0" y2="1">
          <stop offset="0" stop-color="#8a7aa8"/><stop offset="0.4" stop-color="#6f8c86"/><stop offset="1" stop-color="#4f7a35"/>
        </linearGradient>
        <linearGradient id="tone-grain" x1="0" y1="0" x2="1" y2="1">
          <stop offset="0" stop-color="#c8a850"/><stop offset="1" stop-color="#6b5a22"/>
        </linearGradient>
        <linearGradient id="tone-paddy" x1="0" y1="0" x2="1" y2="1">
          <stop offset="0" stop-color="#b9dc6a"/><stop offset="1" stop-color="#4f8a33"/>
        </linearGradient>
        <linearGradient id="tone-sky" x1="0" y1="0" x2="0" y2="1">
          <stop offset="0" stop-color="#4a86c8"/><stop offset="0.4" stop-color="#e6eef5"/><stop offset="0.55" stop-color="#6f9a46"/><stop offset="1" stop-color="#3d7a25"/>
        </linearGradient>
        <linearGradient id="tone-crop" x1="0" y1="0" x2="1" y2="1">
          <stop offset="0" stop-color="#7fa66a"/><stop offset="1" stop-color="#3b5e2c"/>
        </linearGradient>
      </defs>

      <!-- backdrop -->
      <rect class="backdrop" x="0" y="0" width="826" height="1168" fill="var(--forest)"/>
      <path class="archipelago-map" role="img" aria-label="Map of the Southeast Asian archipelago"
            d="M0 20 Q60 40 110 110 Q160 150 200 120 Q260 60 330 40 Q400 20 470 60 Q540 90 620 70 Q700 60 760 110 Q800 140 826 120 L826 270 Q790 300 740 260 Q680 220 620 230 Q560 180 490 200 Q430 220 380 170 Q330 130 280 160 Q220 200 170 180 Q110 160 70 120 Q30 90 0 100 Z"
            fill="var(--forest-deep)" opacity="0.55"/>

      <!-- sweeping bands -->
      <path class="band band-gold" d="M0 450 Q500 420 826 760 L826 1168 L0 1168 Z" fill="url(#sweep-gold)"/>
      <path class="band band-green-glow" d="M0 470 Q420 440 700 640 Q420 500 0 500 Z" fill="#3f8f63" opacity="0.6"/>
      <path class="band band-cream" d="M0 525 Q430 500 770 980 Q420 640 0 650 Z" fill="url(#sweep-cream)"/>
      <path class="band band-cream-wide" d="M0 630 Q460 600 730 1010 L0 1010 Z" fill="var(--cream)" opacity="0.85"/>
      <path class="band band-olive" d="M0 690 Q360 720 620 960 Q300 860 0 900 Z" fill="url(#sweep-olive)"/>
      <path class="band band-amber" d="M0 850 Q420 860 720 1110 L720 1168 L0 1168 Z" fill="url(#sweep-amber)"/>
      <path class="band-rule" d="M0 498 Q420 470 760 700" fill="none" stroke="#ffffff" stroke-width="1.5" stroke-dasharray="2 4" opacity="0.7"/>
      <path class="band-rule" d="M700 700 Q790 880 800 1168" fill="none" stroke="#ffffff" stroke-width="1.5" stroke-dasharray="2 4" opacity="0.6"/>

      <!-- title guide -->
      <line class="title-guide" x1="108" y1="0" x2="108" y2="398" stroke="var(--gold)" stroke-width="1.5" stroke-dasharray="2 4"/>
      <circle class="title-guide-end" cx="108" cy="404" r="3.5" fill="none" stroke="var(--gold)" stroke-width="1.5"/>

      <!-- leaf photo windows -->
      <g class="leaf-spray" stroke="var(--leaf-edge)" stroke-width="4">
        <path class="leaf" role="img" aria-label="Photo of an ancient stone temple statue" d="M418 184 Q571 239 580 402 Q427 347 418 184 Z" fill="url(#tone-stone)"/>
        <path class="leaf" role="img" aria-label="Photo of green hillside rice terraces" d="M700 290 Q728 437 622 542 Q594 395 700 290 Z" fill="url(#tone-terrace)"/>
        <path class="leaf" role="img" aria-label="Photo of curved rice terrace rows" d="M472 396 Q596 459 602 598 Q478 535 472 396 Z" fill="url(#tone-field)"/>
        <path class="leaf" role="img" aria-label="Photo of farmland beside a coastline" d="M774 484 Q772 622 656 696 Q658 558 774 484 Z" fill="url(#tone-coast)"/>
        <path class="leaf" role="img" aria-label="Photo of palm trees over rice terraces" d="M502 586 Q624 662 622 806 Q500 730 502 586 Z" fill="url(#tone-field)"/>
        <path class="leaf" role="img" aria-label="Photo of ripe rice stalks" d="M812 668 Q785 814 642 852 Q669 706 812 668 Z" fill="url(#tone-grain)"/>
        <path class="leaf" role="img" aria-label="Photo of terraced paddies in a valley" d="M488 776 Q600 863 597 1007 Q484 919 488 776 Z" fill="url(#tone-terrace)"/>
        <path class="leaf" role="img" aria-label="Photo of a farmer planting rice seedlings" d="M824 871 Q766 1010 616 1017 Q674 878 824 871 Z" fill="url(#tone-paddy)"/>
        <path class="leaf" role="img" aria-label="Photo of a rice field under blue sky" d="M552 961 Q552 1091 446 1166 Q446 1035 552 961 Z" fill="url(#tone-sky)"/>
        <path class="leaf" role="img" aria-label="Photo of a farmer among leafy crops" d="M808 1051 Q726 1170 582 1166 Q664 1046 808 1051 Z" fill="url(#tone-crop)"/>
        <path class="leaf" role="img" aria-label="Photo of tropical trees" d="M432 1116 Q430 1160 366 1168 Q380 1128 432 1116 Z" fill="url(#tone-crop)"/>
      </g>
    </svg>

    <h1 class="cover-title">
      <span>The</span>
      <span>Southern</span>
      <span>Meridian</span>
      <span>Collective for</span>
      <span>Skills and</span>
      <span>Growth</span>
    </h1>
  </section>
</div>
</body>
</html>
```